Revolutionary Digital Car Parking Ticket

We are looking for a Brochure Type Web design and a design for a Logo for a brand new company and a product that has no equal anywhere in the world. The product is subject to a Patent Application.
The Company is Bellwether Kerbside Limited and will have a URL of www.lonmeroto.com.au
The designs need to be in Adobe Photo Shop and we are seeking the actual adobe file with unmerged layers.
The product is a digital parking ticket which automatically identifies where a car is parked and if applicable automatically bills the user of the device for the cost of parking for the time the vehicle is parked. The user no longer needs to worry about parking fines, or “feeding” the parking metre. Equally there is no longer any need for those ugly street parking metres.
A picture of the device is attached.
The design needs to impart to the user of the Web Site a feeling of a company which is innovative, designing cutting edge technology, very smart, friendly and sensitive to peoples needs in its area of technology development.
Equally the site needs to be:
a) very simple, uncluttered and clean;
b) such that any user intuitively understands how to use and get what they want.
c) such that the user again intuitively trust the product and the company to deliver a product which does what it indicates it can do;
d) such that it provides confidence that the use of the product will save them money and make sure they don’t get parking fines again and are only charged for the time that they are parked; and
e) such that all understand that they are in control of the operation of the product.
The front page of the Web site needs to provide the user with the following access points:
a) Buy a product;
b) Log into their established account;
c) Make contact with the company;
d) Understand all of the Company Privacy Conditions; and
e) Understand who the company is.
Updates
Please remember that the product is about car parking in any place and one needs to ensure that a site user immediately recognises that by buying the device it makes Car Parking much easier. To put this another way the graphics on the site need to immediately let the user know we are on about car parking made easy.
Target Market(s)
Consumers. Ordinary people who drive cars
Industry/Entity Type
Digital
Logo Text
Ever Calm Tidy Motoring
Number of Pages Required
1 page
Font styles to use
Requirements
Must have
- Must be simple and clean and uncluttered
Nice to have
- Nil
Should not have
- Must not be cluttered

```html
<!DOCTYPE html>
<html lang="en">
<head>
<meta charset="utf-8">
<title>Lonmeroto – Parking made easy</title>
<link rel="stylesheet" href="https://fonts.googleapis.com/css2?family=Roboto:ital,wght@0,300;0,400;0,500;0,700;1,400&display=swap">
<style>
:root{
  --blue:#2a9fd0;
  --blue-dark:#1b86b5;
  --ink:#4a4f55;
  --muted:#7d848b;
  --line:#dfe4e8;
  --paper:#ffffff;
  --soft:#f3f5f7;
  --footer:#2293c3;
}
*{margin:0;padding:0;box-sizing:border-box}
html,body{width:1200px;height:2184px;overflow:hidden}
body{position:relative;background:var(--paper);font-family:"Roboto",Arial,sans-serif;color:var(--ink)}
.abs{position:absolute}

/* header */
.site-header{left:0;top:0;width:1200px;height:80px;border-bottom:1px solid var(--line);background:var(--paper)}
.brand{left:40px;top:22px;display:flex;align-items:center;gap:10px;font-size:28px;font-weight:700;color:var(--blue)}
.brand-dot{width:22px;height:22px;border-radius:50%;background:var(--blue)}
.member-login{right:40px;top:31px;font-size:13px;color:var(--blue);display:flex;align-items:center;gap:6px}

/* hero */
.hero-title{left:0;top:100px;width:1200px;text-align:center;font-size:40px;font-weight:400;color:var(--blue)}
.hero-text{left:100px;top:165px;width:1000px;text-align:center;font-size:13px;line-height:20px;color:var(--muted)}
.hero-text p+p{margin-top:10px}

/* how it works */
.how-bg{left:0;top:270px;width:1200px;height:500px;background:radial-gradient(ellipse 420px 200px at 600px 260px,#e4e8ec 0%,#f2f4f6 55%,#ffffff 100%)}
.section-title{font-size:38px;font-weight:400;color:var(--blue);text-align:center}
.how-title{left:0;top:330px;width:1200px}
.step{display:flex;gap:14px;width:440px;font-size:13px;line-height:19px;color:var(--ink)}
.step-num{flex:none;width:38px;height:38px;background:var(--blue);color:#fff;font-size:20px;font-weight:500;display:flex;align-items:center;justify-content:center}
.step-1{left:40px;top:410px}
.step-2{left:720px;top:490px}
.step-3{left:40px;top:570px}
.how-tagline{left:700px;top:668px;width:460px;text-align:right;font-style:italic;font-size:20px;color:var(--blue)}

/* features + pricing band */
.tech-panel{left:0;top:790px;width:580px;height:420px;background:var(--paper);border-top:1px solid var(--line);border-bottom:1px solid var(--line)}
.tech-title{left:40px;top:815px;font-size:30px;color:var(--blue);font-weight:400}
.tech-row{left:60px;display:flex;gap:28px;align-items:flex-start;width:480px;font-size:13px;line-height:19px;color:var(--muted)}
.tech-row svg{flex:none}
.price-bg{left:580px;top:790px;width:620px;height:420px;background:linear-gradient(135deg,#3fb1dc 0%,#2592c2 60%,#1d7fac 100%)}
.pricing-title{left:620px;top:815px;font-size:30px;color:#fff;font-weight:400}
.plan{width:150px;color:#fff;text-align:left}
.plan-name{font-size:22px;font-weight:400;padding-bottom:8px;border-bottom:1px solid rgba(255,255,255,.5)}
.plan ul{list-style:none;margin-top:10px}
.plan li{font-size:12px;line-height:18px;padding:6px 0;border-bottom:1px solid rgba(255,255,255,.25)}
.plan-price{left:0;width:110px;height:40px;background:#fff;color:var(--blue-dark);font-size:18px;font-weight:500;display:flex;align-items:center;justify-content:center}
.plan-buy{width:110px;text-align:center;font-size:12px;color:#fff}

/* about */
.about-title{left:0;top:1280px;width:1200px}
.about-rule{left:560px;top:1336px;width:80px;height:2px;background:var(--blue)}
.about-text{left:140px;top:1352px;width:920px;text-align:center;font-size:13px;line-height:20px;color:var(--muted)}
.portrait{width:220px;height:230px;background:linear-gradient(180deg,#d6d9dc,#bfc3c7);border:6px solid #eceef0}
.person{width:300px;text-align:center}
.person-name{font-size:22px;color:var(--blue);font-weight:400}
.person-role{font-size:13px;color:var(--ink);margin-top:4px}
.person-text{font-size:12px;line-height:18px;color:var(--muted);margin-top:8px}

/* contact */
.contact-band{left:0;top:1770px;width:1200px;height:360px;border-top:4px solid var(--blue);background:var(--soft)}
.map{left:0;top:1774px;width:700px;height:356px;background:linear-gradient(135deg,#e6e9ec 0%,#d9dde1 50%,#e9ecef 100%)}
.contact-title{left:760px;top:1800px;font-size:38px;color:var(--blue);font-weight:400}
.contact-block{left:760px;font-size:12px;line-height:18px;color:var(--ink)}
.contact-block strong{font-weight:500;display:block}
.contact-line{display:flex;align-items:center;gap:8px;font-size:12px;color:var(--ink)}
.socials{left:760px;top:2070px;display:flex;gap:8px}
.socials span{width:28px;height:28px;border-radius:50%;background:var(--ink)}

/* footer */
.site-footer{left:0;top:2130px;width:1200px;height:54px;background:var(--footer);color:#fff;font-size:12px;display:flex;align-items:center;justify-content:center}
</style>
</head>
<body>

<header class="site-header abs">
  <div class="brand abs"><span class="brand-dot"></span>Lonmeroto</div>
  <div class="member-login abs">Member Login
    <svg width="14" height="14" viewBox="0 0 14 14"><circle cx="7" cy="4.5" r="3" fill="none" stroke="#2a9fd0" stroke-width="1.4"/><path d="M1.5 13c0-3 2.5-5 5.5-5s5.5 2 5.5 5" fill="none" stroke="#2a9fd0" stroke-width="1.4"/></svg>
  </div>
</header>

<h1 class="hero-title abs">The future of parking is Here!</h1>
<div class="hero-text abs">
  <p>Drive in, park and walk away. Our digital ticket knows where your car stands, starts the clock on its own and bills only the minutes you use. No meters to feed, no coins to find and no fines waiting on the windscreen when you return.</p>
  <p>Built for everyday drivers, the device works in any street or car park. You stay in control from your phone, see every charge as it happens and stop at any time. Parking made easy, fair and calm for everyone on the road.</p>
</div>

<div class="how-bg abs" role="img" aria-label="Faded photo of the digital parking ticket device"></div>
<h2 class="section-title how-title abs">How it works?</h2>
<div class="step step-1 abs"><span class="step-num">1</span><p>Place the small ticket on your windscreen and link it to your account in a minute.</p></div>
<div class="step step-2 abs"><span class="step-num">2</span><p>The device finds where you parked and starts counting the time by itself.</p></div>
<div class="step step-3 abs"><span class="step-num">3</span><p>Drive away and pay only for the minutes you stayed. No fines, no meters.</p></div>
<p class="how-tagline abs">...And never worry about parking again!</p>

<section class="tech-panel abs"></section>
<h2 class="tech-title abs">Technical description</h2>
<div class="tech-row abs" style="top:885px">
  <svg width="26" height="26" viewBox="0 0 26 26"><rect x="2" y="16" width="4" height="8" fill="#2a9fd0"/><rect x="9" y="11" width="4" height="13" fill="#2a9fd0"/><rect x="16" y="6" width="4" height="18" fill="#2a9fd0"/><rect x="23" y="1" width="3" height="23" fill="#2a9fd0"/></svg>
  <p>Small, light unit that fits any windscreen and runs for months on one battery.</p>
</div>
<div class="tech-row abs" style="top:965px">
  <svg width="26" height="26" viewBox="0 0 26 26"><path d="M13 1a8 8 0 0 0-8 8c0 6 8 16 8 16s8-10 8-16a8 8 0 0 0-8-8z" fill="#2a9fd0"/><circle cx="13" cy="9" r="3" fill="#fff"/></svg>
  <p>Built-in location finds the exact parking zone and its rate in seconds.</p>
</div>
<div class="tech-row abs" style="top:1045px">
  <svg width="26" height="26" viewBox="0 0 26 26"><circle cx="13" cy="13" r="11" fill="none" stroke="#2a9fd0" stroke-width="2"/><path d="M13 6v7l5 3" fill="none" stroke="#2a9fd0" stroke-width="2"/></svg>
  <p>Time is counted to the minute and stops the moment your car leaves.</p>
</div>
<div class="tech-row abs" style="top:1125px">
  <svg width="26" height="26" viewBox="0 0 26 26"><path d="M13 2a7 7 0 0 0-7 7v6l-3 4h20l-3-4V9a7 7 0 0 0-7-7z" fill="#2a9fd0"/><circle cx="13" cy="22" r="2.5" fill="#2a9fd0"/></svg>
  <p>Alerts reach your phone before a zone limit runs out, so fines never come.</p>
</div>

<div class="price-bg abs" role="img" aria-label="Blue tinted aerial city map background"></div>
<h2 class="pricing-title abs">Pricing information</h2>
<div class="plan abs" style="left:640px;top:880px">
  <div class="plan-name">Basic</div>
  <ul><li>One device</li></ul>
</div>
<div class="plan abs" style="left:820px;top:880px">
  <div class="plan-name">Medium</div>
  <ul><li>Two devices</li><li>Monthly report</li><li>Phone alerts</li></ul>
</div>
<div class="plan abs" style="left:1000px;top:880px">
  <div class="plan-name">Super</div>
  <ul><li>Five devices</li><li>Live reports</li><li>Phone alerts</li><li>Priority help</li><li>Free fitting</li></ul>
</div>
<div class="plan-price abs" style="left:640px;top:1122px">6.99$/m</div>
<div class="plan-price abs" style="left:820px;top:1122px">15.99$/m</div>
<div class="plan-price abs" style="left:1000px;top:1122px">29.99$/m</div>
<div class="plan-buy abs" style="left:640px;top:1172px">Buy Now</div>
<div class="plan-buy abs" style="left:820px;top:1172px">Buy Now</div>
<div class="plan-buy abs" style="left:1000px;top:1172px">Buy Now</div>

<h2 class="section-title about-title abs">About Us</h2>
<div class="about-rule abs"></div>
<p class="about-text abs">We are a small team of engineers and drivers who were tired of fines and meters. We build simple, honest technology that makes parking easy for everyone, in every city and on every street.</p>

<div class="portrait abs" style="left:320px;top:1410px" role="img" aria-label="Portrait of the first co-founder"></div>
<div class="portrait abs" style="left:680px;top:1410px" role="img" aria-label="Portrait of the second co-founder"></div>
<div class="person abs" style="left:280px;top:1655px">
  <div class="person-name">Name Family</div>
  <div class="person-role">CEO, Co-Founder</div>
  <p class="person-text">Long time driver and engineer who leads the product from idea to the street.</p>
</div>
<div class="person abs" style="left:640px;top:1655px">
  <div class="person-name">Name Family</div>
  <div class="person-role">CEO, Co-Founder</div>
  <p class="person-text">Keeps the company close to drivers and makes sure every charge is fair.</p>
</div>

<section class="contact-band abs"></section>
<div class="map abs" role="img" aria-label="Street map showing the company headquarters location"></div>
<h2 class="contact-title abs">Contact Us</h2>
<div class="contact-block abs" style="top:1860px"><strong>Headquarters:</strong>Level 4, 120 Harbour Street,<br>Sydney NSW 2000</div>
<div class="contact-block abs" style="top:1925px"><strong>Sales:</strong>Level 2, 18 Market Lane,<br>Melbourne VIC 3000</div>
<div class="abs" style="left:760px;top:2020px;display:flex;gap:40px">
  <div class="contact-line"><svg width="16" height="12" viewBox="0 0 16 12"><rect x="0.5" y="0.5" width="15" height="11" fill="none" stroke="#4a4f55"/><path d="M1 1l7 6 7-6" fill="none" stroke="#4a4f55"/></svg>hello@lonmeroto.com.au</div>
  <div class="contact-line"><svg width="12" height="14" viewBox="0 0 12 14"><path d="M2 1h3l1 3-2 1.5a8 8 0 0 0 3.5 3.5L9 7l3 1v3a2 2 0 0 1-2 2C5 13 0 8 0 3a2 2 0 0 1 2-2z" fill="#4a4f55"/></svg>+61 2 9000 0000</div>
</div>
<div class="socials abs"><span></span><span></span><span></span></div>

<footer class="site-footer abs">Member Login | Terms &amp; Privacy | © Bellwether Kerbside Limited</footer>

</body>
</html>
```